Handy man Company business card

need branded business card for my new company, this design will transfer to car wrap design what winner will be asked to design

I will need original file so I can edit it in the end.

Also like to have some inspirational quote like "ONE CALL WE DO IT ALL"
"We do it right" can be added to logo side

Like to try to see large 1 800 000 0000 number on front with large logo

Size bigger then standard business card

I like to integrate LAS VEGAS sign to one of sides

Target Market(s)

Handy man services, Home renovation and remodeling

Industry/Entity Type

Handyman

Contact Information for Business Card

Tidewell Works LLC.
Name: BORIS KELMANTOV
Phone "Temporary": 000 000 0000
Adress: 5172 Orchid Ln, Las Vegas NV 89147
Website: www.tidewellworks.vegas
Email: info@tidewellworks.vegas

Requirements
Must have
• Two side
• side n1: LOGO
• side n2: INFO
Nice to have
• Like to have some interesting idea for client to remember!
• With logo added to both side at different stile
Should not have
• Standard design,

```html
<!DOCTYPE html>
<html lang="en">
<head>
<meta charset="utf-8">
<title>Tidewell Works – Business Card</title>
<link rel="stylesheet" href="https://fonts.googleapis.com/css2?family=Open+Sans:wght@400;600;700&display=swap">
<style>
  :root {
    --page-bg: #e9e6e2;
    --card-bg: #1b1b1b;
    --card-edge: #101010;
    --ink: #ffffff;
    --accent: #f2a51a;
    --muted: #d9d9d9;
  }
  * { box-sizing: border-box; margin: 0; padding: 0; }
  html, body {
    width: 1200px; height: 1200px; overflow: hidden;
    background: var(--page-bg);
    font-family: "Open Sans", Arial, sans-serif;
  }
  .sheet {
    width: 1200px; height: 1200px;
    display: flex; flex-direction: column;
    align-items: center; justify-content: center; gap: 60px;
  }
  .card {
    width: 840px; height: 480px;
    background: var(--card-bg);
    border-radius: 26px;
    box-shadow: 0 10px 24px rgba(0,0,0,.25);
    position: relative;
    color: var(--ink);
  }
  /* Brand lockup */
  .brand {
    display: flex; align-items: center; gap: 18px;
  }
  .brand-mark {
    width: 30px; height: 30px; border-radius: 50%;
    background: var(--accent); flex: none;
  }
  .brand-name {
    font-weight: 700; color: var(--ink); white-space: nowrap;
  }
  /* Front */
  .card--front {
    display: flex; align-items: center; justify-content: center;
  }
  .card--front .brand-name { font-size: 60px; }
  .card--front .brand-mark { width: 52px; height: 52px; }
  /* Back */
  .card--back .brand {
    position: absolute; left: 60px; top: 190px;
  }
  .card--back .brand-name { font-size: 34px; }
  .divider {
    position: absolute; left: 470px; top: 70px;
    width: 2px; height: 340px; background: var(--ink);
  }
  .holder-name {
    position: absolute; left: 510px; top: 82px;
    font-size: 22px; font-weight: 600; letter-spacing: .5px;
  }
  .contact-list {
    position: absolute; left: 510px; top: 270px;
    list-style: none; display: flex; flex-direction: column; gap: 10px;
  }
  .contact-item {
    display: flex; align-items: center; gap: 12px;
    font-size: 17px; color: var(--muted); white-space: nowrap;
  }
  .contact-icon {
    width: 18px; height: 18px; border-radius: 3px;
    background: var(--accent); flex: none;
    display: flex; align-items: center; justify-content: center;
  }
  .contact-icon svg { width: 12px; height: 12px; }
</style>
</head>
<body>
<main class="sheet">
  <section class="card card--front" aria-label="Card front">
    <div class="brand">
      <span class="brand-mark"></span>
      <span class="brand-name">Tidewell Works</span>
    </div>
  </section>

  <section class="card card--back" aria-label="Card back">
    <div class="brand">
      <span class="brand-mark"></span>
      <span class="brand-name">Tidewell Works</span>
    </div>
    <div class="divider"></div>
    <p class="holder-name">BORIS KELMANTOV</p>
    <ul class="contact-list">
      <li class="contact-item">
        <span class="contact-icon"><svg viewBox="0 0 12 12"><path d="M3 1 L5 3.5 L4 5 Q5 7 7 8 L8.5 7 L11 9 L9.5 11 Q4 10.5 1 3 Z" fill="#1b1b1b"/></svg></span>
        000 000 0000
      </li>
      <li class="contact-item">
        <span class="contact-icon"><svg viewBox="0 0 12 12"><circle cx="6" cy="6" r="4.5" fill="none" stroke="#1b1b1b" stroke-width="1.4"/><path d="M1.5 6 H10.5 M6 1.5 Q3.5 6 6 10.5 Q8.5 6 6 1.5" fill="none" stroke="#1b1b1b" stroke-width="1"/></svg></span>
        www.tidewellworks.vegas
      </li>
      <li class="contact-item">
        <span class="contact-icon"><svg viewBox="0 0 12 12"><rect x="1.5" y="3" width="9" height="6.5" fill="none" stroke="#1b1b1b" stroke-width="1.3"/><path d="M1.5 3 L6 6.5 L10.5 3" fill="none" stroke="#1b1b1b" stroke-width="1.2"/></svg></span>
        info@tidewellworks.vegas
      </li>
      <li class="contact-item">
        <span class="contact-icon"><svg viewBox="0 0 12 12"><path d="M6 11 Q2 6.5 2 4.5 A4 4 0 0 1 10 4.5 Q10 6.5 6 11 Z" fill="#1b1b1b"/><circle cx="6" cy="4.5" r="1.4" fill="#f2a51a"/></svg></span>
        5172 Orchid Ln, Las Vegas NV 89147
      </li>
    </ul>
  </section>
</main>
</body>
</html>
```